MARGOT ELODIE - brand producing beautiful ladies bags to go through the day in an organized way

We need for a brand in-creation a lifestyle luxury website (ie Renard Castel, Halvick, LuneVera) with an online shop. The brand name will be www.margotelodie.example. Ideally, we would like to host the web in HostNimbus. However, we need specific fonts - Didot (brand name) combined with Century Gothic (for the rest) or perhaps propose a better combination if you feel. The web should contain an e-shop. We would like to have a mobile version of the web too.

Target Market(s)

female customers aged 14 - 35

Industry/Entity Type

Fashion

Contact Information for Business Card

Margot Elodie Travan - CEO; Margot.Travan@margotelodie.example; +420 608 192836
Pavel Travan; Pavel.Travan@margotelodie.example; cell +420 609587214
www.Margotelodie.example

Coding

Coded - Design and coding required

Number of Pages Required

5+ page

Font styles to use
Other font styles liked:
• Didot & Century Gothic or similar

Colors

Designer to choose colors to be used in the design.

Requirements
Must have
• the top line bar - please take inspiration from Halvick (no white background). The background should be incorporated in the main image. The brand name will be home button in top left corner. The brand should have feel of lifestyle luxury but functionality - those should be the features of the products (bags). The bags are currently being designed. Functional e-shop - would like to ideally use hostnimbus.example.
Nice to have
• Personal Information should be hidden.

```html
<!DOCTYPE html>
<html lang="en">
<head>
<meta charset="utf-8">
<title>Margot Elodie — Handbags</title>
<link rel="stylesheet" href="https://fonts.googleapis.com/css2?family=Bodoni+Moda:wght@400;500&family=Josefin+Sans:wght@700&family=Questrial&display=swap">
<style>
:root{
  --ink:#1c1c22;
  --white:#ffffff;
  --muted:#8d8d8d;
  --tan:#c79a72;
  --band:#cdc6c1;
  --tile:#f0f0f0;
  --rule:#d9d9d9;
}
*{box-sizing:border-box;margin:0;padding:0}
html,body{width:1200px;height:1200px;overflow:hidden;background:var(--white)}
.stage{position:relative;width:1920px;height:1920px;transform:scale(.625);transform-origin:0 0;font-family:"Questrial",sans-serif;color:var(--ink)}
.abs{position:absolute}
.serif{font-family:"Bodoni Moda",serif}
.eyebrow{font-size:5px;letter-spacing:.6px;color:var(--muted);text-transform:uppercase}
.btn{position:absolute;background:var(--ink);color:var(--white);font-size:5.5px;letter-spacing:.3px;display:flex;align-items:center;justify-content:center;gap:8px;box-shadow:0 2px 4px rgba(0,0,0,.3);text-transform:uppercase;white-space:nowrap}
.btn svg{width:9px;height:5px}
.link-tan{font-size:4.8px;letter-spacing:.4px;color:var(--tan);text-transform:uppercase;display:flex;align-items:center;gap:8px;white-space:nowrap}
.link-tan svg{width:8px;height:4px}

/* hero */
.hero{left:720px;top:0;width:492px;height:307px;background:
  radial-gradient(ellipse 22% 30% at 40% 22%,rgba(214,176,128,.55),transparent 100%),
  radial-gradient(ellipse 20% 45% at 15% 55%,rgba(70,52,44,.85),transparent 100%),
  radial-gradient(ellipse 30% 35% at 50% 70%,rgba(150,104,70,.6),transparent 100%),
  radial-gradient(ellipse 22% 25% at 85% 78%,rgba(60,78,104,.55),transparent 100%),
  linear-gradient(100deg,#4e443e 0%,#7d6c60 45%,#6e625a 75%,#585049 100%)}
.nav-brand{left:45px;top:9px;display:flex;align-items:center;gap:5px;color:var(--white);font-size:7.5px;letter-spacing:.4px;white-space:nowrap}
.nav-brand i{display:block;width:6px;height:6px;border:1px solid var(--white)}
.nav-links{left:312px;top:11px;display:flex;gap:9px;color:var(--white);font-size:5px;letter-spacing:.3px}
.cart{left:422px;top:8px;width:10px;height:10px}
.hero-title{left:252px;top:86px;font-family:"Josefin Sans",sans-serif;font-weight:700;font-size:27.5px;line-height:26px;color:var(--white);white-space:nowrap}
.dots{left:238px;top:282px;display:flex;gap:3px}
.dots i{width:3px;height:3px;border-radius:50%;border:.6px solid var(--white)}
.dots i.on{background:var(--white)}

/* features */
.features{left:768px;top:333px;width:399px;height:88px;background:var(--band)}
.feature{position:absolute;top:14px;width:107px;height:59px;border:1px solid var(--white);text-align:center;color:#eeeae7}
.feature svg{display:block;margin:7px auto 2px;width:14px;height:12px}
.feature h3{font-weight:400;font-size:4.5px;letter-spacing:.3px;margin-bottom:5px}
.feature p{font-size:3.8px;line-height:5px;padding:0 12px}

/* categories */
.cat-head{left:866px;top:453px;width:214px}
.section-title{font-family:"Bodoni Moda",serif;font-weight:400;font-size:17px;line-height:20.5px;letter-spacing:.2px}
.body-text{font-size:5.8px;line-height:8.6px}
.tile{position:absolute}
.tile-card{position:absolute;background:var(--white);padding:8px 10px 0}
.tile-card h4{font-family:"Bodoni Moda",serif;font-weight:400;font-size:7.6px;letter-spacing:.4px;text-transform:uppercase;margin-bottom:4px;white-space:nowrap;color:var(--ink)}

/* bestsellers */
.product{position:absolute}

/* newsletter */
.newsletter{left:720px;top:1314px;width:492px;height:179px;color:var(--white);text-align:center}
.newsletter-bg{background:
  radial-gradient(ellipse 14% 22% at 22% 55%,rgba(20,18,18,.8),transparent 100%),
  radial-gradient(ellipse 14% 30% at 82% 55%,rgba(150,100,66,.75),transparent 100%),
  radial-gradient(ellipse 25% 40% at 50% 30%,rgba(110,88,72,.6),transparent 100%),
  linear-gradient(90deg,#3c2e28 0%,#5a4a40 35%,#4a3d36 60%,#6b5241 100%)}
.newsletter h2{font-family:"Bodoni Moda",serif;font-weight:400;font-size:16.5px;letter-spacing:.6px;margin-top:44px;white-space:nowrap}
.newsletter p{font-size:5.8px;line-height:8.6px;margin:8px auto 0;width:198px}
.field{left:133px;top:116px;width:184px;height:21px;background:#dcdcdc;font-size:4.5px;color:#9a9a9a;text-align:left;padding:8px 12px}
.submit{left:317px;top:116px;width:43px;height:21px;background:var(--ink);font-size:5px;padding-top:8px}

/* blog */
.post{position:absolute;left:767px;display:flex;gap:9px}
.thumb{width:59px;height:59px;background:
  radial-gradient(ellipse 40% 35% at 62% 55%,#9fb3c2,transparent 100%),
  radial-gradient(ellipse 30% 25% at 25% 70%,#5a5e62,transparent 100%),
  linear-gradient(135deg,#e6e8e8,#c9d0d4 60%,#eeeeee)}
.post h5{font-weight:400;font-size:6.8px;line-height:7.4px;width:132px;margin-top:1px}
.post small{display:block;font-size:4.5px;letter-spacing:.4px;color:var(--muted);margin-top:4px}
.featured{left:972px;top:1553px;width:194px;height:237px;background:
  radial-gradient(ellipse 28% 18% at 55% 38%,#ece9e6,transparent 100%),
  radial-gradient(ellipse 18% 16% at 22% 62%,#8a4f30,transparent 100%),
  linear-gradient(90deg,#2a2524 0%,#3a302d 35%,#cdb899 70%,#e0cfb4 100%)}
.tag{left:15px;top:14px;border:1px solid var(--white);color:var(--white);font-size:4.8px;padding:3px 4px;letter-spacing:.3px}
.feat-card{left:15px;top:167px;width:164px;height:55px;background:var(--white);padding:12px 16px 0}
.feat-card h5{font-weight:400;font-size:9px;line-height:10.4px;margin-bottom:5px}

/* footer */
.footer-rule{left:770px;top:1838px;width:398px;height:1px;background:var(--rule)}
.f-mark{left:795px;top:1859px;width:16px;height:16px;border:1px solid var(--ink)}
.f-name{left:770px;top:1882px;font-family:"Bodoni Moda",serif;font-size:6.3px;letter-spacing:.2px;white-space:nowrap}
.f-copy{left:772px;top:1892px;font-size:3.8px;line-height:4.4px;color:var(--muted);text-align:center;width:58px}
.f-col{top:1871px;font-size:4.8px;line-height:8.6px;letter-spacing:.4px;text-transform:uppercase;list-style:none;white-space:nowrap}
</style>
</head>
<body>
<div class="stage">

  <!-- hero -->
  <section class="abs hero" role="img" aria-label="Campaign photograph: model in fringed suede jacket holding a patterned leather handbag"></section>
  <div class="abs" style="left:720px;top:0;width:492px;height:307px">
    <a class="abs nav-brand serif"><i></i>MARGOT ELODIE</a>
    <nav class="abs nav-links"><span>SHOP</span><span>ABOUT</span><span>CONTACT</span><span>BLOG</span></nav>
    <svg class="abs cart" viewBox="0 0 10 10" fill="none" stroke="#fff" stroke-width="1.2"><rect x="1" y="3" width="8" height="6.5"/><path d="M3.2 3V2a1.8 1.8 0 0 1 3.6 0v1"/></svg>
    <h1 class="abs hero-title">Bold &amp; Daring<br>New Designs</h1>
    <a class="btn" style="left:252px;top:150px;width:126px;height:21px">Shop the 2020 collection <svg viewBox="0 0 9 5" fill="none" stroke="#fff" stroke-width=".8"><path d="M0 2.5h8M6 .5l2 2-2 2"/></svg></a>
    <div class="abs dots"><i></i><i class="on"></i><i></i></div>
  </div>

  <!-- features -->
  <section class="abs features">
    <div class="feature" style="left:11px">
      <svg viewBox="0 0 14 12" fill="none" stroke="#eeeae7" stroke-width=".8"><rect x="1" y="2" width="8" height="6"/><path d="M9 4h3l1.5 2v2H9"/><circle cx="3.5" cy="9" r="1.2"/><circle cx="11" cy="9" r="1.2"/></svg>
      <h3>SHIPPING &amp; RETURNS</h3>
      <p>If your bags aren't perfect, return them within 30 days for a full refund</p>
    </div>
    <div class="feature" style="left:147px">
      <svg viewBox="0 0 14 12" fill="none" stroke="#eeeae7" stroke-width=".8"><rect x="1" y="2" width="12" height="8"/><path d="M1 4.5h12"/><circle cx="11" cy="9.5" r="1.5"/></svg>
      <h3>SAFE PAYMENT</h3>
      <p>Pay with the world's most popular and secure payment methods</p>
    </div>
    <div class="feature" style="left:283px">
      <svg viewBox="0 0 14 12" fill="none" stroke="#eeeae7" stroke-width=".8"><path d="M3 4h8l1 7H2z"/><path d="M5 4V3a2 2 0 0 1 4 0v1"/><path d="M9 9.5h3"/></svg>
      <h3>SHOP WITH CONFIDENCE</h3>
      <p>Our Buyer Protection covers your purchase from click to delivery</p>
    </div>
  </section>

  <!-- categories -->
  <header class="abs cat-head">
    <div class="eyebrow">Categories</div>
    <h2 class="section-title" style="margin-top:3px">Stylish, modern handbags<br>for the trendsetter</h2>
    <p class="body-text" style="margin-top:6px">Lorem ipsum dolor sit amet, consectetur adipiscing elit, sed do eiusmod tempor incididunt ut labore et dolore magna aliqua. Quis ipsum suspendisse ultrices gravida. Risus commodo viverra maecenas accumsan lacus vel facilisis.</p>
  </header>

  <div class="tile" style="left:766px;top:565px;width:125px;height:119px;background:
    radial-gradient(ellipse 40% 18% at 62% 40%,#151515,transparent 100%),
    radial-gradient(ellipse 30% 40% at 20% 25%,#8a3a26,transparent 100%),
    radial-gradient(ellipse 40% 20% at 40% 95%,#7489a4,transparent 100%),
    linear-gradient(180deg,#ffffff,#e9e4df)" role="img" aria-label="Woman carrying a black shoulder bag"></div>
  <div class="tile" style="left:903px;top:565px;width:125px;height:119px;background:
    radial-gradient(ellipse 35% 22% at 55% 32%,#a86a3a,transparent 100%),
    radial-gradient(ellipse 40% 70% at 20% 50%,#3a302c,transparent 100%),
    radial-gradient(ellipse 30% 60% at 85% 60%,#2a2320,transparent 100%),
    linear-gradient(90deg,#5a4a42,#efe9e2 60%,#3a302c)" role="img" aria-label="Tan leather clutch held under the arm"></div>
  <div class="tile" style="left:1039px;top:565px;width:126px;height:117px;background:
    radial-gradient(ellipse 20% 40% at 50% 45%,#f7f7f5,transparent 100%),
    radial-gradient(ellipse 10% 12% at 55% 18%,#2b2624,transparent 100%),
    radial-gradient(ellipse 14% 10% at 68% 52%,#7b7b80,transparent 100%),
    linear-gradient(180deg,#e4e8ee,#d3d8de)" role="img" aria-label="Woman in a white suit holding a work bag"></div>
  <div class="tile" style="left:766px;top:697px;width:262px;height:117px;background:
    radial-gradient(ellipse 14% 45% at 42% 45%,#1e1c1c,transparent 100%),
    radial-gradient(ellipse 8% 50% at 52% 45%,#6b5a62,transparent 100%),
    radial-gradient(ellipse 16% 45% at 68% 50%,#f3f1ee,transparent 100%),
    linear-gradient(100deg,#6f6f6f,#bdbcb8 30%,#8c8a86 60%,#d8d6d2 85%)" role="img" aria-label="Quilted black bag with a beaded chain strap"></div>
  <div class="tile" style="left:1039px;top:697px;width:126px;height:117px;background:
    radial-gradient(ellipse 26% 28% at 36% 50%,#ece5d8,transparent 100%),
    radial-gradient(ellipse 18% 50% at 68% 40%,#27303f,transparent 100%),
    radial-gradient(ellipse 20% 8% at 55% 95%,#7a4a2a,transparent 100%),
    linear-gradient(180deg,#e6e6e6,#d4d2ce)" role="img" aria-label="Canvas tote bag carried by a man"></div>

  <div class="tile-card" style="left:781px;top:633px;width:95px;height:35px"><h4>Shoulder Bags</h4><div class="link-tan">View product <svg viewBox="0 0 8 4" fill="none" stroke="#c79a72" stroke-width=".6"><path d="M0 2h7M5.5.5 7 2 5.5 3.5"/></svg></div></div>
  <div class="tile-card" style="left:919px;top:633px;width:95px;height:35px"><h4>Clutch Bags</h4><div class="link-tan">View product <svg viewBox="0 0 8 4" fill="none" stroke="#c79a72" stroke-width=".6"><path d="M0 2h7M5.5.5 7 2 5.5 3.5"/></svg></div></div>
  <div class="tile-card" style="left:1056px;top:633px;width:95px;height:35px"><h4>Work Bags</h4><div class="link-tan">View product <svg viewBox="0 0 8 4" fill="none" stroke="#c79a72" stroke-width=".6"><path d="M0 2h7M5.5.5 7 2 5.5 3.5"/></svg></div></div>
  <div class="tile-card" style="left:781px;top:764px;width:95px;height:35px"><h4>Elegant Bags</h4><div class="link-tan">View product <svg viewBox="0 0 8 4" fill="none" stroke="#c79a72" stroke-width=".6"><path d="M0 2h7M5.5.5 7 2 5.5 3.5"/></svg></div></div>
  <div class="tile-card" style="left:1056px;top:761px;width:95px;height:35px"><h4>Large Bags</h4><div class="link-tan">View product <svg viewBox="0 0 8 4" fill="none" stroke="#c79a72" stroke-width=".6"><path d="M0 2h7M5.5.5 7 2 5.5 3.5"/></svg></div></div>

  <a class="btn" style="left:920px;top:832px;width:86px;height:21px">View all products <svg viewBox="0 0 9 5" fill="none" stroke="#fff" stroke-width=".8"><path d="M0 2.5h8M6 .5l2 2-2 2"/></svg></a>

  <!-- bestsellers -->
  <header class="abs" style="left:767px;top:928px;width:126px">
    <div class="eyebrow">Bestsellers</div>
    <h2 class="section-title" style="font-size:15.6px;line-height:21px;margin-top:5px">Stylish, modern<br>handbags for<br>the trendsetter</h2>
    <p class="body-text" style="margin-top:7px">Lorem ipsum dolor sit amet, consectetur adipiscing elit, sed do eiusmod tempor incididunt ut labore et dolore magna aliqua. Quis ipsum suspendisse ultrices</p>
  </header>

  <div class="product" style="left:903px;top:904px;width:127px;height:172px;background:radial-gradient(ellipse 42% 34% at 50% 62%,rgba(40,40,42,.85),transparent 100%),linear-gradient(180deg,#f2f2f2,#ececec)" role="img" aria-label="Black leather tote bag"></div>
  <div class="product" style="left:1041px;top:904px;width:126px;height:172px;background:radial-gradient(ellipse 40% 34% at 50% 60%,rgba(226,70,78,.85),transparent 100%),linear-gradient(180deg,#f0f0f0,#e6e6e6)" role="img" aria-label="Red leather handbag"></div>
  <div class="product" style="left:766px;top:1087px;width:126px;height:172px;background:radial-gradient(ellipse 22% 14% at 50% 32%,rgba(214,170,90,.6),transparent 100%),radial-gradient(ellipse 40% 28% at 50% 55%,rgba(225,225,222,.95),transparent 100%),linear-gradient(180deg,#f6f6f6,#efefef)" role="img" aria-label="White crossbody bag with gold chain handle"></div>
  <div class="product" style="left:903px;top:1087px;width:127px;height:172px;background:radial-gradient(ellipse 14% 10% at 50% 38%,rgba(122,70,42,.6),transparent 100%),radial-gradient(ellipse 40% 30% at 50% 60%,rgba(232,192,40,.85),transparent 100%),linear-gradient(180deg,#f2f2f2,#ededed)" role="img" aria-label="Yellow and white checked bucket bag"></div>
  <div class="product" style="left:1041px;top:1087px;width:126px;height:172px;background:radial-gradient(ellipse 34% 38% at 50% 58%,rgba(230,218,206,.95),transparent 100%),linear-gradient(180deg,#f4f4f4,#efefef)" role="img" aria-label="Cream leather hobo bag"></div>

  <a class="btn" style="left:775px;top:1234px;width:110px;height:20px">Add to cart <svg viewBox="0 0 9 5" fill="none" stroke="#fff" stroke-width=".8"><path d="M0 2.5h8M6 .5l2 2-2 2"/></svg></a>

  <!-- newsletter -->
  <section class="abs newsletter newsletter-bg" role="img" aria-label="Street style photograph of women carrying leather bags"></section>
  <div class="abs newsletter">
    <h2>Subscribe to our newsletter</h2>
    <p>Stay up to date with our newest collections, latest deals and special offers! We announce new collection every three weeks so be sure to stay in touch to catch the hottest pieces for you.</p>
    <div class="abs field">ENTER YOUR EMAIL</div>
    <div class="abs submit">SUBMIT</div>
  </div>

  <!-- blog -->
  <h2 class="abs section-title" style="left:767px;top:1550px;font-size:17px;white-space:nowrap">Genius Blog Posts</h2>
  <article class="post" style="top:1582px"><div class="thumb" role="img" aria-label="Blue handbag beside sunglasses"></div><div><h5>Lorem ipsum dolor sit amet consecte adipisicing elitdeserunt</h5><small>AUTHOR NAME</small></div></article>
  <article class="post" style="top:1647px"><div class="thumb" role="img" aria-label="Blue handbag beside sunglasses"></div><div><h5>Lorem ipsum dolor sit amet consecte adipisicing elitdeserunt</h5><small>AUTHOR NAME</small></div></article>
  <article class="post" style="top:1712px"><div class="thumb" role="img" aria-label="Blue handbag beside sunglasses"></div><div><h5>Lorem ipsum dolor sit amet consecte adipisicing elitdeserunt</h5><small>AUTHOR NAME</small></div></article>
  <a class="abs link-tan" style="left:767px;top:1784px">Read the latest articles <svg viewBox="0 0 8 4" fill="none" stroke="#c79a72" stroke-width=".6"><path d="M0 2h7M5.5.5 7 2 5.5 3.5"/></svg></a>

  <div class="abs featured" role="img" aria-label="Street style photograph of a white half-moon bag and a brown bag"></div>
  <div class="abs" style="left:972px;top:1553px;width:194px;height:237px">
    <span class="abs tag">FEATURED</span>
    <div class="abs feat-card"><h5>Lorem ipsum dolor sit amet, consectetur adipiscing elit</h5><div class="link-tan">Read article <svg viewBox="0 0 8 4" fill="none" stroke="#c79a72" stroke-width=".6"><path d="M0 2h7M5.5.5 7 2 5.5 3.5"/></svg></div></div>
  </div>

  <!-- footer -->
  <div class="abs footer-rule"></div>
  <div class="abs f-mark"></div>
  <div class="abs f-name">MARGOT ELODIE</div>
  <div class="abs f-copy">©2020 MARGOT ELODIE.<br>ALL RIGHTS RESERVED</div>
  <ul class="abs f-col" style="left:953px"><li>Shop</li><li>About</li><li>Blog</li><li>Contact</li></ul>
  <ul class="abs f-col" style="left:994px"><li>Customer service</li><li>Track my order</li><li>My account</li><li>Return policy</li></ul>
  <ul class="abs f-col" style="left:1063px"><li>12th Linden Row</li><li>Harbor City, CA</li><li>United States, 90000</li></ul>
  <ul class="abs f-col" style="left:1135px"><li>Pagefeed</li><li>Chirpline</li><li>Snapgrid</li></ul>

</div>
</body>
</html>
```